Postcard Design

Landscaping Company
Lawn Cuts
Mulch
Spring Clean Ups
Planting

Company Name - RVM GROUNDWORK PARTNERS
ADDRESS - 47 Kestwick Rd.
N. Hanover, NJ 08599
Phone #- 609-555-0148

Target Market(s)

Direct mailer looking to draw in new clients

Industry/Entity Type

It Company

Requirements
Must have
• Eye catching

```html
<!DOCTYPE html>
<html lang="en">
<head>
<meta charset="utf-8">
<title>RVM Groundwork Partners – Postcard</title>
<link rel="stylesheet" href="https://fonts.googleapis.com/css2?family=Lato:ital,wght@0,400;0,700;0,900;1,400&family=Roboto+Condensed:wght@400;700&display=swap">
<style>
  :root{
    --bg:#2b2b2b;
    --blue:#1f4f9c;
    --blue-mid:#3a6cc0;
    --blue-dark:#173d7e;
    --blue-light:#5b8fd6;
    --red:#c8161d;
    --red-dark:#8f0d12;
    --white:#ffffff;
    --grey-light:#ececec;
    --grey:#b8b8b8;
    --ink:#2f2f2f;
    --sky:#a9c7e8;
    --foliage:#5d7f3a;
  }
  *{box-sizing:border-box;margin:0;padding:0}
  html,body{width:902px;height:1200px;overflow:hidden;background:var(--bg)}
  body{position:relative;font-family:"Lato",sans-serif}

  .card{position:absolute;width:658px;height:510px;overflow:hidden;box-shadow:0 6px 18px rgba(0,0,0,.5)}
  .card--front{left:122px;top:50px;background:linear-gradient(#ffffff,#e4e4e4)}
  .card--back{left:122px;top:630px;background:var(--white)}
  .card__art{position:absolute;left:0;top:0}

  /* front */
  .brand{position:absolute;right:30px;top:38px;display:flex;align-items:center;gap:8px;
    font-family:"Lato",sans-serif;font-weight:700;font-size:19px;color:var(--ink)}
  .brand__mark{width:14px;height:14px;background:var(--blue)}
  .badge{position:absolute;left:40px;top:48px;width:130px;height:130px}
  .badge__text{position:absolute;inset:0;display:flex;flex-direction:column;align-items:center;justify-content:center;
    font-family:"Roboto Condensed",sans-serif;font-size:17px;line-height:1.45;color:var(--white);text-transform:uppercase}
  .contact-row{position:absolute;left:0;top:425px;width:658px;display:flex}
  .contact-row__item{flex:1;text-align:center;color:var(--white);font-family:"Roboto Condensed",sans-serif;font-weight:700;font-size:19px;white-space:nowrap}
  .contact-row__item--phone{font-size:25px;color:#111;font-weight:400;margin-top:-4px}

  /* back */
  .back-site{position:absolute;right:22px;top:18px;color:var(--white);font-weight:700;font-style:italic;font-size:18px}
  .stamp{position:absolute;left:555px;top:68px;width:75px;height:90px;border:2px solid #111}
  .address-line{position:absolute;left:398px;width:232px;height:1px;background:#222}
  .pill{position:absolute;left:22px;height:28px;padding:0 18px 0 14px;border-radius:0 14px 14px 0;
    background:linear-gradient(#ffffff,#d6d6d6);font-weight:900;font-size:18px;color:var(--ink);display:flex;align-items:center;white-space:nowrap}
  .services{position:absolute;left:28px;top:50px;width:322px;color:var(--white);font-size:9.3px;line-height:1.28}
  .services p{margin-bottom:5px}
  .services ul{list-style:none}
  .services li{position:relative;padding-left:12px;margin-bottom:4px;font-size:8.2px;line-height:1.25}
  .services li::before{content:"✓";position:absolute;left:0;top:0;font-weight:700}
  .pm-list{position:absolute;left:30px;top:338px;list-style:none;display:grid;
    grid-template-columns:158px 130px;grid-template-rows:repeat(4,auto);grid-auto-flow:column;
    font-family:"Roboto Condensed",sans-serif;font-size:11px;color:var(--white);line-height:1.25;white-space:nowrap}
  .pm-list li{padding-left:12px;position:relative}
  .pm-list li::before{content:"";position:absolute;left:0;top:4px;width:6px;height:6px;border-radius:50%;background:#111}
  .postal{position:absolute;left:30px;top:440px;color:var(--white);font-style:italic;font-size:16px;line-height:1.4;white-space:nowrap}
  .postal__home{display:inline-block;width:11px;height:11px;margin-right:6px}
</style>
</head>
<body>

<section class="card card--front">
  <svg class="card__art" width="658" height="510" viewBox="0 0 658 510">
    <defs>
      <linearGradient id="photo-tone" x1="0" y1="0" x2="0" y2="1">
        <stop offset="0" stop-color="var(--sky)"/>
        <stop offset=".45" stop-color="#7f8f78"/>
        <stop offset="1" stop-color="var(--foliage)"/>
      </linearGradient>
    </defs>
    <polygon points="0,190 330,70 658,190 658,392 0,392" fill="url(#photo-tone)" role="img" aria-label="Photo of a stone house with a landscaped garden, hedges and lawn"/>
    <polyline points="0,188 330,63 658,188" fill="none" stroke="var(--blue)" stroke-width="11"/>
    <rect x="0" y="392" width="658" height="98" fill="var(--blue)"/>
    <rect x="219" y="392" width="220" height="98" fill="var(--blue-mid)"/>
    <rect x="0" y="490" width="658" height="20" fill="var(--grey-light)"/>
    <g fill="var(--white)" stroke="var(--grey)" stroke-width="2">
      <polygon points="118,355 148,372 148,406 118,423 88,406 88,372"/>
      <polygon points="340,355 370,372 370,406 340,423 310,406 310,372"/>
      <polygon points="566,355 596,372 596,406 566,423 536,406 536,372"/>
    </g>
    <g fill="none" stroke="#333" stroke-width="2">
      <rect x="104" y="380" width="28" height="19"/>
      <polyline points="104,380 118,392 132,380"/>
      <rect x="332" y="374" width="16" height="30" rx="2"/>
      <rect x="335" y="378" width="10" height="8"/>
      <circle cx="566" cy="389" r="13"/>
      <ellipse cx="566" cy="389" rx="6" ry="13"/>
      <line x1="553" y1="389" x2="579" y2="389"/>
    </g>
  </svg>

  <div class="brand"><span class="brand__mark"></span>RVM Groundwork Partners</div>

  <div class="badge">
    <svg width="130" height="130" viewBox="0 0 130 130">
      <polygon fill="var(--red)" stroke="var(--red-dark)" stroke-width="2" points="65,2 74,18 91,8 92,27 111,24 104,42 122,48 108,62 122,76 104,84 110,102 91,100 90,119 74,110 65,126 56,110 40,119 39,100 20,102 26,84 8,76 22,62 8,48 26,42 19,24 38,27 39,8 56,18"/>
    </svg>
    <div class="badge__text"><span>Book your</span><span>appointment</span></div>
  </div>

  <div class="contact-row">
    <div class="contact-row__item">hello@rvmgroundwork.com</div>
    <div class="contact-row__item contact-row__item--phone">(609) 555-0148</div>
    <div class="contact-row__item">www.rvmgroundwork.com</div>
  </div>
</section>

<section class="card card--back">
  <svg class="card__art" width="658" height="510" viewBox="0 0 658 510">
    <defs>
      <radialGradient id="back-blue" cx=".35" cy=".35" r=".8">
        <stop offset="0" stop-color="var(--blue-light)"/>
        <stop offset="1" stop-color="var(--blue-dark)"/>
      </radialGradient>
    </defs>
    <path d="M0,0 H430 Q300,255 425,510 H0 Z" fill="url(#back-blue)"/>
    <path d="M430,0 Q300,255 425,510" fill="none" stroke="var(--grey)" stroke-width="9"/>
    <path d="M432,18 H658 V50 H414 Q420,32 432,18 Z" fill="var(--blue)"/>
  </svg>

  <div class="back-site">www.rvmgroundwork.com</div>
  <div class="stamp"></div>
  <div class="address-line" style="top:252px"></div>
  <div class="address-line" style="top:314px"></div>
  <div class="address-line" style="top:378px"></div>

  <h2 class="pill" style="top:16px">Our Services</h2>
  <div class="services">
    <p>RVM Management will handle the day-to-day activities that are required in operating your Association. RVM Management offers building and ground maintenance as well as operations management services to meet your association’s needs. We are the best at what we do and will provide your association with the support you need and require.</p>
    <p>Services Include but not limited to…</p>
    <ul>
      <li>Maintain the common areas of the property within the constraints of the approved budget; review operating expenditures including insurance, utilities and services and where possible, reduce the cost to the Association while maintaining the quality of services.</li>
      <li>Hire, pay (at the expense of the Association), negotiate, supervise and discharge employees or sub-contractors necessary to maintain the premises in accordance with the approved budget.</li>
      <li>Negotiate on behalf of and at the expense of the Association service contracts for utilities, trash removal, janitorial, landscaping and any other such service deemed necessary for the property.</li>
      <li>Provide 24-hour, seven-days a week emergency services for immediate assistance.</li>
    </ul>
  </div>

  <h2 class="pill" style="top:302px;font-size:16px">Property Management</h2>
  <ul class="pm-list">
    <li>Consulting</li><li>Maintenance</li><li>Collecting Dues/Rent</li><li>Construction Management</li>
    <li>Landscaping</li><li>Snow Removal</li><li>Commercial Cleaning</li><li>Staff Management</li>
  </ul>

  <h2 class="pill" style="top:402px">Contact Us</h2>
  <address class="postal">
    <svg class="postal__home" viewBox="0 0 12 12"><path d="M6 0 L12 6 H10 V12 H7 V8 H5 V12 H2 V6 H0 Z" fill="#111"/></svg>RVM GROUNDWORK PARTNERS<br>
    &nbsp;&nbsp;&nbsp;47 Kestwick Rd. N. Hanover, NJ 08599
  </address>
</section>

</body>
</html>
```